Skylorn Holiday Greetings Card

We are looking for a digital / Print Holliday Greetings card to email out to our customers. We really want something different but must remain within the aviation industry. OUr customers are primarily Airlines and the message needs to be generic and non-religious.
It is a joyful time and we want to thank them for their continuous support and wish them the best over the holidays and a happy New Year, Text will be provided in word format as an upload file.

See our Website for overall brand . Althogh we we have uploaded some past samples it is only as a reference. We need somehting new.

www.skylornworks.example

Target Market(s)

airlines our customers

Industry/Entity Type

Aviation

Colors
0555a3
3276b5
85abd2
ec1f27

Requirements
Must have
• Our logo
• Our colors
• aviation and technical feel
• bilingual message (supplied by us in the uploaded files)
• Something unique
• our website
Nice to have
• Animation on the digital side
• Although the colors listed below are our brand colors we are open to suggestions.
Should not have
• Religious messages or images
• Santa Clause
• Reindeers

```html
<!DOCTYPE html>
<html lang="en">
<head>
<meta charset="utf-8">
<title>Skylorn Holiday Greetings Card</title>
<link rel="stylesheet" href="https://fonts.googleapis.com/css2?family=Crimson+Text:wght@400;600&family=Roboto+Condensed:ital,wght@1,500&display=swap">
<style>
  :root{
    --brand-deep:#0555a3;
    --brand-mid:#3276b5;
    --brand-light:#85abd2;
    --sky-dark:#1c4a90;
    --sky-bright:#3a78c0;
    --band-shade:#043f7c;
    --ink-white:#ffffff;
    --page:#ffffff;
  }
  html,body{margin:0;padding:0;width:1200px;height:1200px;overflow:hidden;background:var(--page);}
  .canvas{position:relative;width:1200px;height:1200px;}
  .card{position:absolute;left:242px;width:714px;height:503px;overflow:hidden;background:var(--brand-deep);}
  .card--message{top:96px;}
  .card--cover{top:625px;}
  .card__art{position:absolute;inset:0;width:714px;height:503px;display:block;}
  .brand{position:absolute;left:31px;top:22px;display:flex;align-items:center;gap:7px;
    font-family:"Crimson Text",serif;font-weight:600;font-size:15px;color:var(--ink-white);letter-spacing:.5px;}
  .brand__mark{width:14px;height:14px;background:var(--ink-white);}
  .message__para{position:absolute;left:280px;width:420px;margin:0;text-align:center;white-space:nowrap;
    font-family:"Crimson Text",serif;font-weight:400;font-size:17px;line-height:22.4px;color:var(--ink-white);}
  .message__para--en1{top:42px;}
  .message__para--en2{top:152px;}
  .message__para--fr1{top:277px;}
  .message__para--fr2{top:364px;}
  .message__divider{position:absolute;left:411px;top:242px;width:162px;height:8px;border-radius:4px;background:var(--ink-white);opacity:.85;}
  .greeting{position:absolute;left:425px;top:240px;margin:0;
    font-family:"Roboto Condensed",sans-serif;font-style:italic;font-weight:500;font-size:48px;line-height:56px;color:var(--ink-white);
    transform:scaleX(.8);transform-origin:left top;white-space:nowrap;}
  .greeting span{display:block;}
  .greeting span:last-child{margin-left:-15px;}
</style>
</head>
<body>
<main class="canvas">

  <section class="card card--message">
    <svg class="card__art" viewBox="0 0 714 503">
      <defs>
        <linearGradient id="skyStrip" x1="0" y1="0" x2="0" y2="1">
          <stop offset="0" stop-color="#1c4a90"/>
          <stop offset="1" stop-color="#3a78c0"/>
        </linearGradient>
      </defs>
      <rect width="714" height="503" fill="#0555a3"/>
      <polygon points="184,0 310,0 174,503 70,503" fill="url(#skyStrip)" role="img" aria-label="Photo of a jet high in a blue sky trailing white contrails"/>
      <polygon points="184,0 192,0 78,503 70,503" fill="#043f7c" opacity=".5"/>
      <polygon points="310,0 714,0 714,503 174,503" fill="#85abd2"/>
    </svg>
    <div class="brand"><span class="brand__mark"></span>Skylorn</div>
    <p class="message__para message__para--en1">During this Holiday season, we take the time to<br>reflect upon the good things we have… like our<br>partnership with you. We truly appreciate your trust in<br>us and we thank you for your continued support.</p>
    <p class="message__para message__para--en2">Our team wishes you and your family a safe, and<br>Happy Holiday and we hope that 2019 will bring you</p>
    <span class="message__divider" role="img" aria-label="Ornamental divider"></span>
    <p class="message__para message__para--fr1">Pendant cette période des Fêtes, nous prenons le temps<br>de réfléchir sur les bonnes choses que nous<br>avons…comme notre partenariat avec vous.</p>
    <p class="message__para message__para--fr2">Nous apprécions votre confiance en nous et nous vous en<br>remercions. Notre équipe vous souhaite à vous et à votre<br>famille un Joyeux temps des Fêtes et nous espérons que<br>2019 vous apportera santé, bonheur et succès.</p>
  </section>

  <section class="card card--cover">
    <svg class="card__art" viewBox="0 0 714 503">
      <defs>
        <linearGradient id="skyWide" x1="0.3" y1="0" x2="0.7" y2="1">
          <stop offset="0" stop-color="#1c4a90"/>
          <stop offset="1" stop-color="#3a78c0"/>
        </linearGradient>
      </defs>
      <rect width="714" height="503" fill="#0555a3"/>
      <polygon points="196,0 262,0 136,503 67,503" fill="#3276b5"/>
      <polygon points="262,0 330,0 204,503 136,503" fill="#85abd2"/>
      <polygon points="328,0 714,0 714,503 202,503" fill="url(#skyWide)" role="img" aria-label="Photo of a jet climbing through a deep blue sky with long white contrails"/>
    </svg>
    <div class="brand"><span class="brand__mark"></span>Skylorn</div>
    <h1 class="greeting"><span>Joyeuses Fetes</span><span>Happy Holiday</span></h1>
  </section>

</main>
</body>
</html>
```